Data Collection Workbook

We are creating a data gathering booklet that will be completed by our clients (ages 40-90). Due to the volume of information being collected, we are looking for a format that is both inviting to complete and aesthetically pleasing to the eye. The final product will be approximately 20-30 pages, divided into 13 sections. A table of contents, as well as two sample pages are attached.

```html
<!DOCTYPE html>
<html lang="en">
<head>
<meta charset="utf-8">
<title>My General Information</title>
<link href="https://fonts.googleapis.com/css2?family=Arimo:wght@700&family=Nunito:wght@800&display=swap" rel="stylesheet">
<style>
  :root {
    --mint: #66ffcc;
    --mint-line: #6cefc0;
    --mint-tint: #dcfff2;
    --purple: #cc66ff;
    --ink: #111111;
    --paper: #ffffff;
    --edge: #8a8a8a;
  }
  html, body { margin: 0; padding: 0; overflow: hidden; background: var(--paper); }
  .page {
    position: relative; width: 849px; height: 1200px; box-sizing: border-box;
    border: 1px solid var(--edge); background: var(--paper); overflow: hidden;
    font-family: "Arimo", Arial, sans-serif;
  }
  .header-band { position: absolute; left: 50px; right: 0; top: 0; height: 60px; background: var(--mint); }
  .header-rule { position: absolute; left: 50px; right: 0; top: 134px; height: 11px; background: var(--mint); }
  .header-tab { position: absolute; left: 0; top: 0; width: 50px; height: 145px; background: var(--purple); }
  .page-title {
    position: absolute; left: 50px; right: 0; top: 64px; margin: 0; text-align: center;
    font-family: "Nunito", "Arial Rounded MT Bold", sans-serif; font-weight: 800;
    font-size: 53px; line-height: 66px; color: var(--purple); padding-left: 30px;
  }
  .row { position: absolute; left: 28px; width: 738px; border-bottom: 2px solid var(--mint-line); box-sizing: border-box; }
  .field { position: absolute; top: 5px; bottom: 0; border-left: 2px solid var(--mint-line); }
  .field.first { left: 0; }
  .field.mid { left: 388px; }
  .field.end { left: 597px; right: 0; }
  .label {
    position: absolute; left: 7px; top: 2px; white-space: nowrap;
    font-size: 11.5px; line-height: 14px; color: var(--ink);
    background: var(--mint-tint); padding-right: 18px;
  }
  .label .gap { display: inline-block; width: 30px; }
  .row.writing { border-bottom: 2px solid var(--mint-line); }
  .page-number {
    position: absolute; left: 36px; top: 1084px; width: 80px; height: 80px;
    background: var(--purple); border-radius: 40px 40px 40px 0;
    color: var(--paper); font-family: "Arimo", Arial, sans-serif; font-weight: 400;
    font-size: 32px; line-height: 80px; text-align: center;
  }
</style>
</head>
<body>
<div class="page">
  <div class="header-band"></div>
  <div class="header-rule"></div>
  <div class="header-tab"></div>
  <h1 class="page-title">My General Information</h1>

  <div class="row" style="top:158px;height:47px"><div class="field first"><span class="label">My full legal name</span></div></div>
  <div class="row" style="top:203px;height:47px"><div class="field first"><span class="label">My date of birth</span></div><div class="field mid"><span class="label">Location (City/State)</span></div></div>
  <div class="row" style="top:248px;height:47px"><div class="field first"><span class="label">My social security number</span></div></div>
  <div class="row" style="top:293px;height:47px"><div class="field first"><span class="label">My driver’s license number (or DMV identification number)</span></div><div class="field mid"><span class="label">State</span></div></div>
  <div class="row" style="top:338px;height:46px"><div class="field first"><span class="label">My passport number</span></div><div class="field mid"><span class="label">City/State Issued</span></div></div>
  <div class="row" style="top:382px;height:47px"><div class="field first"><span class="label">My address</span></div><div class="field mid"><span class="label">City, State Zip</span></div></div>
  <div class="row" style="top:427px;height:47px"><div class="field first"><span class="label">My telephone number: Cell phone</span></div><div class="field mid"><span class="label">Voicemail Password</span></div></div>
  <div class="row" style="top:472px;height:47px"><div class="field first"><span class="label">Home phone</span></div><div class="field mid"><span class="label">Voicemail Password</span></div></div>
  <div class="row" style="top:517px;height:46px"><div class="field first"><span class="label">Work phone</span></div><div class="field mid"><span class="label">Voicemail Password</span></div></div>
  <div class="row" style="top:561px;height:47px"><div class="field first"><span class="label">Other phone</span></div><div class="field mid"><span class="label">Password</span></div></div>
  <div class="row" style="top:606px;height:47px"><div class="field first"><span class="label">My <b>in-state</b> emergency contact</span></div><div class="field mid"><span class="label">Phone</span></div><div class="field end"><span class="label">Relationship</span></div></div>
  <div class="row" style="top:651px;height:47px"><div class="field first"><span class="label">My <b>out-in-state</b> emergency contact</span></div><div class="field mid"><span class="label">Phone</span></div><div class="field end"><span class="label">Relationship</span></div></div>
  <div class="row" style="top:696px;height:47px"><div class="field first"><span class="label">Child or close relative/friend 1<span class="gap"></span>Address</span></div><div class="field mid"><span class="label">Phone</span></div><div class="field end"><span class="label">Relationship</span></div></div>
  <div class="row" style="top:741px;height:46px"><div class="field first"><span class="label">Child or close relative/friend 2<span class="gap"></span>Address</span></div><div class="field mid"><span class="label">Phone</span></div><div class="field end"><span class="label">Relationship</span></div></div>
  <div class="row" style="top:785px;height:47px"><div class="field first"><span class="label">Child or close relative/friend 3<span class="gap"></span>Address</span></div><div class="field mid"><span class="label">Phone</span></div><div class="field end"><span class="label">Relationship</span></div></div>
  <div class="row" style="top:830px;height:47px"><div class="field first"><span class="label">Child or close relative/friend 4<span class="gap"></span>Address</span></div><div class="field mid"><span class="label">Phone</span></div><div class="field end"><span class="label">Relationship</span></div></div>
  <div class="row" style="top:875px;height:47px"><div class="field first"><span class="label">Location &amp; access instructions (combination) for in-home safe or strong box</span></div></div>
  <div class="row" style="top:920px;height:46px"><div class="field first"><span class="label">Location of safe deposit box(es)</span></div><div class="field mid"><span class="label">Location of keys</span></div></div>
  <div class="row" style="top:964px;height:47px"><div class="field first"><span class="label">List of safe deposit box contents</span></div></div>
  <div class="row writing" style="top:1009px;height:47px"></div>
  <div class="row writing" style="top:1054px;height:47px"></div>
  <div class="row writing" style="top:1099px;height:46px"></div>

  <div class="page-number">3</div>
</div>
</body>
</html>
```